Morvik Construction Business Card

I need a business card design for my company.
We are a construction/machinery company.
I would like to see my logo on the front of the card and my details on the other side
I would like the card to be black or dark grey in colour,with my logo as i send it or modified with a lighter blue colour
I would like to see the design kept fairly simple,but eye catching at the same time
Industry/Entity Type
Business
Colors
00a990
1b1b1b
000000
474747
ececec

```html
<!DOCTYPE html>
<html lang="en">
<head>
<meta charset="utf-8">
<title>Morvik Construction Business Card</title>
<link rel="stylesheet" href="https://fonts.googleapis.com/css2?family=Montserrat:wght@400;700&display=swap">
<style>
  :root {
    --page-bg: #ffffff;
    --card-dark: #1b1b1b;
    --accent-teal: #00a990;
    --card-light: #ececec;
    --ink: #333333;
  }
  * { margin: 0; padding: 0; box-sizing: border-box; }
  html, body {
    width: 1124px;
    height: 1200px;
    overflow: hidden;
    background: var(--page-bg);
  }
  .canvas {
    position: relative;
    width: 1124px;
    height: 1200px;
    font-family: "Montserrat", Arial, sans-serif;
  }
  .card {
    position: absolute;
    left: 115px;
    width: 895px;
    height: 497px;
  }
  .card-front {
    top: 93px;
    background: var(--card-dark);
  }
  .accent-band {
    position: absolute;
    left: 279px;
    top: 0;
    width: 336px;
    height: 100%;
    background: var(--accent-teal);
    display: flex;
    flex-direction: column;
    align-items: center;
    justify-content: center;
  }
  .brand-mark {
    width: 40px;
    height: 40px;
    background: var(--ink);
    margin-bottom: 18px;
    margin-top: -10px;
  }
  .brand-name {
    color: var(--ink);
    font-weight: 700;
    text-transform: uppercase;
    text-align: center;
    line-height: 1.05;
  }
  .brand-name .primary {
    display: block;
    font-size: 50px;
    letter-spacing: 2px;
  }
  .brand-name .secondary {
    display: block;
    font-size: 19px;
    letter-spacing: 3px;
    margin-top: 4px;
  }
  .card-back {
    top: 611px;
    background: var(--card-light);
    display: flex;
    align-items: center;
    justify-content: center;
  }
  .contact-details {
    color: var(--ink);
    font-size: 26px;
    font-weight: 400;
    line-height: 33px;
    text-align: center;
    margin-top: -44px;
  }
</style>
</head>
<body>
  <main class="canvas">
    <section class="card card-front">
      <div class="accent-band">
        <div class="brand-mark"></div>
        <div class="brand-name">
          <span class="primary">Morvik</span>
          <span class="secondary">Construction</span>
        </div>
      </div>
    </section>
    <section class="card card-back">
      <div class="contact-details">
        <p class="contact-name">Name xxxxxxxxx</p>
        <p class="contact-address">address : 418 Kestrel Way</p>
        <p class="contact-email">Email : info.office@morvikbuild.com</p>
      </div>
    </section>
  </main>
</body>
</html>
```